Trade show post card for sportfishing

I would like a double sided postcard used to be a larger more descriptive, eye catching, marketing tool to be used at trade show. I want the double sided postcard to be descriptive and eye catching for both avid fisherman and inviting enough not to scare away first timers looking to enjoy the experience.

Target Market(s)

Males 25-60

Colors

Designer to choose colors to be used in the design.

Requirements
Must have
• My logo, website, phone number, type of trips, pictures of fishing trips we have had which I included below. But I do not need all of the pictures designers can use ones they feel will be most appealing
Nice to have
• Color scheme that works with my logo.

```html
<!DOCTYPE html>
<html lang="en">
<head>
<meta charset="utf-8">
<title>Riverbend Sport Fishing – Trade Show Postcard</title>
<link href="https://fonts.googleapis.com/css2?family=Lato:wght@400;700;900&display=swap" rel="stylesheet">
<style>
  :root{
    --stage:#58585a;
    --green:#6fb746;
    --tick:#7cc04f;
    --ink:#111111;
    --text:#1d1d1d;
    --white:#ffffff;
    --label:#f4f4f4;
  }
  *{box-sizing:border-box;margin:0;padding:0}
  html,body{width:1200px;height:1200px;overflow:hidden;background:var(--stage);font-family:'Lato',sans-serif}
  .canvas{position:relative;width:1200px;height:1200px}
  .side-label{position:absolute;color:var(--label);font-weight:700;font-size:38px}
  .side-label--front{left:816px;top:496px}
  .side-label--back{left:298px;top:1080px}

  .card{position:absolute;overflow:hidden;background:var(--white);box-shadow:6px 8px 10px rgba(0,0,0,.45)}
  .card--front{left:86px;top:63px;width:666px;height:516px}
  .card--back{left:451px;top:625px;width:665px;height:515px}
  .layer{position:absolute;inset:0;width:100%;height:100%}

  .front-photo{position:absolute;inset:0;
    background:
      linear-gradient(180deg,#cfdbe6 0%,#b9c9d6 6%,#6f8b56 9%,#5b7a48 16%,transparent 22%),
      linear-gradient(180deg,#8e97a0 20%,#6f7a84 50%,#7e8890 100%);}
  .front-photo::after{content:"";position:absolute;left:120px;top:60px;width:420px;height:320px;border-radius:45% 45% 30% 30%;
    background:radial-gradient(ellipse at 50% 50%,#b9c2c8 0%,#5f7d9b 45%,transparent 75%)}

  .brand{position:absolute;color:var(--ink);font-weight:900;font-size:32px;letter-spacing:.3px;display:flex;align-items:center;gap:8px;white-space:nowrap;z-index:2}
  .brand__dot{width:13px;height:13px;border-radius:50%;background:var(--green)}
  .card--front .brand{left:462px;top:92px}
  .card--back .brand{left:540px;top:412px;font-size:18px;gap:5px}
  .card--back .brand__dot{width:9px;height:9px}

  .contact{position:absolute;color:var(--white);z-index:2}
  .contact__row{display:flex;align-items:center;position:absolute;left:0;white-space:nowrap}
  .contact__icon{width:22px;height:22px;display:flex;align-items:center;justify-content:center}
  .contact__phone{font-weight:900;font-size:31px;letter-spacing:.3px}
  .contact__text{font-size:19px;font-weight:700}
  .card--front .contact{left:24px;top:400px}
  .card--back .contact{left:24px;top:398px}
  .row-phone{top:0;gap:10px}
  .row-mail{top:42px;gap:30px;left:8px}
  .row-web{top:72px;gap:30px;left:8px}

  .social{position:absolute;display:flex;gap:8px;z-index:2}
  .social span{width:25px;height:25px;border-radius:50%;border:2px solid var(--ink);background:#5a9a37}
  .card--front .social{left:586px;top:481px}
  .card--back .social{left:526px;top:479px}

  .top-band{position:absolute;left:0;top:0;width:100%;height:16px;display:flex}
  .top-band__green{width:321px;background:var(--green)}
  .top-band__black{flex:1;background:var(--ink)}

  .features{position:absolute;top:32px;left:10px;right:18px;display:flex;gap:12px;z-index:2}
  .features ul{list-style:none;flex:1}
  .features li{position:relative;padding-left:18px;font-size:14px;line-height:17px;color:var(--text);text-align:justify;margin-bottom:5px}
  .features li::before{content:"";position:absolute;left:2px;top:4px;width:9px;height:5px;border-left:2px solid var(--tick);border-bottom:2px solid var(--tick);transform:rotate(-45deg)}
  .features ul.col-right li{margin-bottom:13px}

  .back-photo{position:absolute;left:0;top:284px;width:665px;height:194px;
    background:
      linear-gradient(180deg,#ffffff 0%,rgba(255,255,255,.6) 18%,rgba(255,255,255,0) 40%),
      linear-gradient(90deg,#aeb8c0 0%,#c9d0d6 25%,#8d8e90 45%,#6d6f74 65%,#b7bfc5 85%,#a4acb2 100%);}
</style>
</head>
<body>
<div class="canvas">

  <section class="card card--front">
    <div class="front-photo" role="img" aria-label="Photo of an angler on a boat holding a large striped bass on the river"></div>
    <svg class="layer" viewBox="0 0 666 516" aria-hidden="true">
      <ellipse cx="612" cy="78" rx="200" ry="188" fill="#111"/>
      <ellipse cx="620" cy="70" rx="196" ry="182" fill="#fff"/>
      <path d="M0 364 C150 338 300 370 420 420 S600 470 666 460 L666 516 L0 516Z" fill="#111"/>
      <path d="M0 376 C150 352 300 384 420 432 S600 480 666 472 L666 516 L0 516Z" fill="#6fb746"/>
    </svg>
    <div class="brand"><span class="brand__dot"></span>Riverbend</div>
    <div class="contact">
      <div class="contact__row row-phone">
        <svg class="contact__icon" style="width:38px;height:38px" viewBox="0 0 38 38"><circle cx="19" cy="19" r="17" fill="none" stroke="#111" stroke-width="2.5"/><path d="M13 10c-2 1-3 3-2 6 2 5 6 9 11 11 3 1 5 0 6-2l-3-4-3 1c-2-1-4-3-5-5l1-3z" fill="#111"/></svg>
        <span class="contact__phone">5550142837</span>
      </div>
      <div class="contact__row row-mail">
        <svg class="contact__icon" viewBox="0 0 22 22"><rect x="1" y="5" width="20" height="13" fill="#111"/><path d="M1 5l10 8 10-8" fill="none" stroke="#6fb746" stroke-width="1.5"/></svg>
        <span class="contact__text">riverbendfish@example.com</span>
      </div>
      <div class="contact__row row-web">
        <svg class="contact__icon" viewBox="0 0 22 22" fill="none" stroke="#111" stroke-width="1.5"><circle cx="11" cy="11" r="9"/><ellipse cx="11" cy="11" rx="4" ry="9"/><path d="M2 11h18M4 6h14M4 16h14"/></svg>
        <span class="contact__text">www.riverbendsportfishing.com</span>
      </div>
    </div>
    <div class="social"><span></span><span></span></div>
  </section>
  <div class="side-label side-label--front">Front</div>

  <section class="card card--back">
    <div class="top-band"><div class="top-band__green"></div><div class="top-band__black"></div></div>
    <div class="back-photo" role="img" aria-label="Photo of a group of anglers on a boat at the marina holding striped bass"></div>
    <div class="features">
      <ul class="col-left">
        <li>Riverbend Sport Fishing offers half and full day charters on the Hudson River during April and May sailing from Poughkeepsie NY.</li>
        <li>Come aboard our 27 foot Harbor walk around style fishing hull powered by twin 200 Horse-power engines with a working head, cabin, and full enclosure to get out of the elements.</li>
        <li>Riverbend uses only LIVE bait including but not limited to; blood worms, sand worms, Herring, Eels. (included with your charter)</li>
        <li>Riverbend has top of the line custom made fishing rods paired with Castline reels for your use.</li>
      </ul>
      <ul class="col-right">
        <li>We have the best electronics on the market by Navix to maximize our fish finding capability and safe navigation.</li>
        <li>Targeting Striped Bass during their spring migration up the Hudson River</li>
        <li>Captain Dan Mercer is a USCG Licensed Captain with over 25 years of experience fishing the Hudson River for Striped Bass.</li>
        <li>Kid and beginner friendly</li>
        <li>1-4 guests</li>
      </ul>
    </div>
    <svg class="layer" viewBox="0 0 665 515" aria-hidden="true">
      <path d="M0 372 C120 352 260 362 380 406 S560 468 665 460 L665 515 L0 515Z" fill="#111"/>
      <path d="M0 382 C120 362 260 372 380 416 S560 478 665 470 L665 515 L0 515Z" fill="#6fb746"/>
    </svg>
    <div class="brand"><span class="brand__dot"></span>Riverbend</div>
    <div class="contact">
      <div class="contact__row row-phone">
        <svg class="contact__icon" style="width:38px;height:38px" viewBox="0 0 38 38"><circle cx="19" cy="19" r="17" fill="none" stroke="#111" stroke-width="2.5"/><path d="M13 10c-2 1-3 3-2 6 2 5 6 9 11 11 3 1 5 0 6-2l-3-4-3 1c-2-1-4-3-5-5l1-3z" fill="#111"/></svg>
        <span class="contact__phone">5550142837</span>
      </div>
      <div class="contact__row row-mail">
        <svg class="contact__icon" viewBox="0 0 22 22"><rect x="1" y="5" width="20" height="13" fill="#111"/><path d="M1 5l10 8 10-8" fill="none" stroke="#6fb746" stroke-width="1.5"/></svg>
        <span class="contact__text">riverbendfish@example.com</span>
      </div>
      <div class="contact__row row-web">
        <svg class="contact__icon" viewBox="0 0 22 22" fill="none" stroke="#111" stroke-width="1.5"><circle cx="11" cy="11" r="9"/><ellipse cx="11" cy="11" rx="4" ry="9"/><path d="M2 11h18M4 6h14M4 16h14"/></svg>
        <span class="contact__text">www.riverbendsportfishing.com</span>
      </div>
    </div>
    <div class="social"><span></span><span></span></div>
  </section>
  <div class="side-label side-label--back">Back</div>

</div>
</body>
</html>
```